Business Card Design Project

I am looking for a minimal matte background/shiny (spot UV) ink monochromatic design with a splash of neon color.

the card should be 2 sided, logo only on one side - all info and possibly logo on the other.

My creative director described the colors he imagined for the design to be:
'it's a dark field, like charcoal or a really dark burgundy, or deep blue, shot through with a neon—but just a tiny bit of it. so a charcoal field with a laser-thin streak of electric lime, safety orange, or cobalt blue. really beautiful stuff.'

here are some samples of the types of cards I am trying to create:
http://www.snapvault.example/photos/dawnpress/4182736450/in/photostream -> Vornelle Lustre

http://www.snapvault.example/photos/dawnpress/3859201746/in/photostream -> Standard Coated (14pt/matte) with SPOT UV

http://www.snapvault.example/photos/dawnpress/3859201372/in/photostream/ -> Dense Orvane with Raised Ink

http://www.snapvault.example/photos/dawnpress/5128463907/in/photostream/ -> Standard Coated (14pt/matte) with SPOT UV

Here is my logo:
https://www.filecrate.example/s/qtrwx730pkd4zn/gulvane%20logotype%20final.ai

Here are the details for info:
Owen Carlisle Dray
email - owen@gulvane.example
mobile - 555 318 6724
web -
gulvane.example: inventive technology applications
gulvane-video.example: innovative video advertising

please let me know if there is anything at all that you need.

Target Market(s)

mid to large agencies that require interactive design and entrepreneurial/startup individuals/companies that need application development.

Industry/Entity Type

Safety

Requirements
Must have
• logo only on one side

```html
<!DOCTYPE html>
<html lang="en">
<head>
<meta charset="utf-8">
<title>Owen Carlisle Dray — Business Card</title>
<link rel="stylesheet" href="https://fonts.googleapis.com/css2?family=Arimo:wght@400&display=swap">
<style>
  :root {
    --backdrop: #8a4a78;
    --card-charcoal: #2a292a;
    --ink-white: #f4f4f4;
    --neon-lime: #b5dc12;
    --safety-orange: #ff6a0d;
    --cobalt-blue: #1f9be3;
    --text-font: "Arimo", Arial, Helvetica, sans-serif;
  }
  html, body {
    margin: 0;
    padding: 0;
    width: 1200px;
    height: 900px;
    overflow: hidden;
    background: var(--backdrop);
  }
  .stage {
    position: relative;
    width: 1200px;
    height: 900px;
  }
  .business-card {
    position: absolute;
    left: 110px;
    top: 170px;
    width: 980px;
    height: 560px;
    background: var(--card-charcoal);
    border-radius: 4px;
    box-shadow: 0 18px 40px rgba(0, 0, 0, 0.35);
    overflow: hidden;
    font-family: var(--text-font);
    color: var(--ink-white);
  }
  .holder-name {
    position: absolute;
    left: 100px;
    top: 205px;
    margin: 0;
    font-size: 27px;
    font-weight: 400;
    letter-spacing: 0.2px;
    line-height: 1;
  }
  .accent-stripes {
    position: absolute;
    left: 0;
    top: 245px;
    width: 420px;
    height: 66px;
  }
  .contact-list {
    position: absolute;
    left: 438px;
    top: 182px;
    margin: 0;
    padding: 0;
    list-style: none;
    font-size: 19px;
    line-height: 23px;
  }
</style>
</head>
<body>
  <main class="stage">
    <section class="business-card" aria-label="Business card front">
      <h1 class="holder-name">Owen Carlisle Dray</h1>
      <svg class="accent-stripes" viewBox="0 0 420 66" aria-hidden="true">
        <rect x="0" y="0" width="420" height="22" fill="var(--neon-lime)"/>
        <rect x="0" y="22" width="420" height="22" fill="var(--safety-orange)"/>
        <rect x="0" y="44" width="420" height="22" fill="var(--cobalt-blue)"/>
      </svg>
      <ul class="contact-list">
        <li>email - owen@gulvane.example</li>
        <li>mobile - 555 318 6724</li>
        <li>web - www.owengulvane.example</li>
        <li>gulvane.example: inventive technology applications</li>
        <li>gulvane-video.example: innovative video advertising</li>
      </ul>
    </section>
  </main>
</body>
</html>
```